Business Card design for new private practice opening

I need a business card design for my new private practice with my new logo uploaded as a file
On the front the logo
On the back: maybe a small logo somewhere?
Priv. Doz. DDr. Marlene Osterwald
Fachärztin für Allgemein- & Viszeralchirurgie
Address: xxx
Tel: xxx
Mobil:xxx
Webseite:xxx
Email:xxx

Contact Information for Business Card

See project description above for details

Requirements
Nice to have
• I would like the colors of the logo incorporated into the business card

```html
<!DOCTYPE html>
<html lang="de">
<head>
<meta charset="utf-8">
<title>Osterwald Chirurgie – Visitenkarte</title>
<link rel="stylesheet" href="https://fonts.googleapis.com/css2?family=Montserrat:wght@500&family=Open+Sans:wght@400&display=swap">
<style>
  :root {
    --backdrop: #e8ebed;
    --card: #ffffff;
    --teal: #4fb8b2;
    --grey-text: #7d7f82;
    --grey-dark: #6f7174;
    --grey-line: #c9cbcd;
  }
  * { margin: 0; padding: 0; box-sizing: border-box; }
  html, body { width: 1200px; height: 1200px; overflow: hidden; }
  body {
    background: var(--backdrop);
    position: relative;
    font-family: "Open Sans", Arial, sans-serif;
  }
  .card {
    position: absolute;
    width: 595px;
    height: 361px;
    background: var(--card);
    overflow: hidden;
  }
  .card-front { left: 149px; top: 195px; }
  .card-back { left: 449px; top: 644px; }

  /* Front */
  .front-mark {
    position: absolute;
    left: 81px; top: 101px;
    width: 136px; height: 136px;
    border-radius: 50%;
    background: var(--teal);
  }
  .front-wordmark {
    position: absolute;
    left: 237px; top: 118px;
    font-family: "Montserrat", Arial, sans-serif;
    font-weight: 500;
    font-size: 44px;
    line-height: 50px;
    letter-spacing: 0.5px;
    color: var(--grey-text);
    text-transform: uppercase;
  }
  .front-band {
    position: absolute;
    left: 0; right: 0; bottom: 0;
    height: 20px;
    background: var(--teal);
  }

  /* Back */
  .back-mark {
    position: absolute;
    left: 41px; top: 42px;
    width: 86px; height: 86px;
    border-radius: 50%;
    background: var(--teal);
  }
  .back-divider {
    position: absolute;
    left: 162px; top: 42px;
    width: 1px; height: 268px;
    background: var(--grey-line);
  }
  .back-info {
    position: absolute;
    left: 194px; top: 40px;
  }
  .person-name {
    font-size: 29px;
    line-height: 36px;
    font-weight: 400;
    color: var(--grey-text);
  }
  .person-title {
    margin-top: 8px;
    font-size: 15px;
    line-height: 20px;
    color: var(--grey-dark);
  }
  .contact-list {
    list-style: none;
    margin-top: 22px;
  }
  .contact-item {
    display: flex;
    align-items: center;
    height: 34px;
    font-size: 17px;
    color: var(--grey-dark);
  }
  .contact-icon {
    width: 20px; height: 20px;
    margin-right: 12px;
    fill: none;
    stroke: var(--grey-text);
    stroke-width: 1.6;
    stroke-linecap: round;
    stroke-linejoin: round;
  }
  .contact-icon.solid { fill: var(--grey-text); stroke: none; }
</style>
</head>
<body>

<section class="card card-front" aria-label="Vorderseite">
  <div class="front-mark"></div>
  <div class="front-wordmark">Osterwald<br>Chirurgie</div>
  <div class="front-band"></div>
</section>

<section class="card card-back" aria-label="Rückseite">
  <div class="back-mark"></div>
  <div class="back-divider"></div>
  <div class="back-info">
    <h1 class="person-name">Priv. Doz. DDr.<br>Marlene Osterwald</h1>
    <p class="person-title">Fachärztin für Allgemein- &amp; Viszeralchirurgie</p>
    <ul class="contact-list">
      <li class="contact-item">
        <svg class="contact-icon solid" viewBox="0 0 20 20"><path d="M10 1.5c-3.3 0-6 2.6-6 5.9 0 4.4 6 11.1 6 11.1s6-6.7 6-11.1c0-3.3-2.7-5.9-6-5.9zm0 8.3a2.4 2.4 0 1 1 0-4.8 2.4 2.4 0 0 1 0 4.8z"/></svg>
        Address: xxx
      </li>
      <li class="contact-item">
        <svg class="contact-icon solid" viewBox="0 0 20 20"><path d="M5.2 2.2l2.6-.4 1.5 3.8-1.9 1.4c.9 2 2.4 3.6 4.4 4.6l1.5-1.9 3.8 1.5-.4 2.7c-.2.9-1 1.6-2 1.5C8.4 15 4.1 10.6 3.8 4.2c0-1 .5-1.8 1.4-2z"/></svg>
        Tel: xxx
      </li>
      <li class="contact-item">
        <svg class="contact-icon" viewBox="0 0 20 20"><rect x="5.5" y="1.5" width="9" height="17" rx="1.5"/><line x1="9" y1="15.5" x2="11" y2="15.5"/></svg>
        Mobil: xxx
      </li>
      <li class="contact-item">
        <svg class="contact-icon" viewBox="0 0 20 20"><circle cx="10" cy="10" r="8"/><ellipse cx="10" cy="10" rx="3.4" ry="8"/><line x1="2" y1="10" x2="18" y2="10"/><path d="M3.4 5.8h13.2M3.4 14.2h13.2"/></svg>
        Webseite: xxx
      </li>
      <li class="contact-item">
        <svg class="contact-icon" viewBox="0 0 20 20"><rect x="2" y="4.5" width="16" height="11" rx="1"/><path d="M2.5 5l7.5 6 7.5-6"/></svg>
        Email: xxx
      </li>
    </ul>
  </div>
</section>

</body>
</html>
```